App Design for quiz app (casual gaming app)

We need an design & logo for our quiz app. Its a simple quiz app, where you pick up a category, answer three questions out of this category. After this an opponent is assigned to your game, and has to answer the same three questions. After this first round is finished, it's the opponents turn to choose a new category and answer three questions out of this category. Now it's your turn to answer the same three questions. With this done, the 2nd round is finished. One game has seven rounds.
Please find attached the balsamiq project. For all of you, do not have balsamiq, please find also the mockups as pdf.
Final delivery should be psd files
Target Market(s)
Casual Games

```html
<!DOCTYPE html>
<html lang="en">
<head>
<meta charset="utf-8">
<title>QuizNest – Welcome</title>
<link rel="stylesheet" href="https://fonts.googleapis.com/css2?family=Source+Sans+3:wght@400;600&family=Roboto:wght@300;400&display=swap">
<style>
  :root {
    --coral: #f67673;
    --blush: #fec8c8;
    --coral-text: #f3716d;
    --white: #ffffff;
    --go-green: #43a047;
    --avatar-light: #b9c86a;
    --avatar-dark: #4f6a2c;
  }
  * { margin: 0; padding: 0; box-sizing: border-box; }
  html, body { width: 674px; height: 1200px; overflow: hidden; }
  body { font-family: "Source Sans 3", "Segoe UI", sans-serif; background: var(--blush); }

  .screen { position: relative; width: 674px; height: 1200px; background: var(--blush); overflow: hidden; }

  .header-band { position: absolute; left: 0; top: 0; width: 674px; height: 502px; background: var(--coral); }

  .status-bar {
    position: absolute; left: 0; top: 0; width: 674px; height: 38px;
    font-family: "Roboto", "Helvetica Neue", sans-serif; font-weight: 300;
    color: var(--white); font-size: 22px;
  }
  .status-bar .signal { position: absolute; left: 12px; top: 10px; }
  .status-bar .carrier { position: absolute; left: 92px; top: 4px; font-weight: 400; }
  .status-bar .wifi { position: absolute; left: 136px; top: 8px; }
  .status-bar .clock { position: absolute; left: 0; width: 674px; top: 3px; text-align: center; }
  .status-bar .charge { position: absolute; right: 84px; top: 4px; }
  .status-bar .battery { position: absolute; right: 14px; top: 9px; }

  .greeting {
    position: absolute; left: 0; width: 674px; top: 96px; text-align: center;
    color: var(--white); font-weight: 600; font-size: 47px; letter-spacing: 0.5px;
  }
  .welcome {
    position: absolute; left: 0; width: 674px; top: 175px; text-align: center;
    color: var(--white); font-weight: 600; font-size: 30px;
  }
  .avatar-prompt {
    position: absolute; left: 0; width: 674px; top: 264px; text-align: center;
    color: var(--white); font-weight: 600; font-size: 26px; line-height: 43px;
  }

  .avatar {
    position: absolute; left: 219px; top: 384px; width: 236px; height: 236px;
    border-radius: 50%; border: 6px solid var(--white);
    background: radial-gradient(circle at 45% 40%, var(--avatar-light), var(--avatar-dark));
  }

  .pitch {
    position: absolute; left: 40px; width: 594px; top: 706px; text-align: center;
    color: var(--coral-text); font-weight: 600; font-size: 29px; line-height: 42.5px;
  }

  .cta {
    position: absolute; left: 110px; top: 955px; width: 457px; height: 88px;
    border-radius: 44px; background: var(--go-green); color: var(--white);
    font-weight: 600; font-size: 41px; line-height: 88px; text-align: center;
  }

  .skip {
    position: absolute; right: 36px; top: 1135px;
    color: var(--coral-text); font-weight: 600; font-size: 33px;
  }
</style>
</head>
<body>
<main class="screen">
  <div class="header-band"></div>

  <div class="status-bar">
    <svg class="signal" width="76" height="16" viewBox="0 0 76 16">
      <circle cx="7" cy="8" r="6" fill="#fff"/>
      <circle cx="22" cy="8" r="6" fill="#fff"/>
      <circle cx="37" cy="8" r="5.3" fill="none" stroke="#fff" stroke-width="1.2"/>
      <circle cx="52" cy="8" r="5.3" fill="none" stroke="#fff" stroke-width="1.2"/>
      <circle cx="67" cy="8" r="5.3" fill="none" stroke="#fff" stroke-width="1.2"/>
    </svg>
    <span class="carrier">Nova</span>
    <svg class="wifi" width="26" height="20" viewBox="0 0 26 20">
      <path d="M1 7 A17 17 0 0 1 25 7" fill="none" stroke="#fff" stroke-width="3"/>
      <path d="M5.5 11 A11 11 0 0 1 20.5 11" fill="none" stroke="#fff" stroke-width="3"/>
      <path d="M13 19 L9 15 A5.5 5.5 0 0 1 17 15 Z" fill="#fff"/>
    </svg>
    <span class="clock">12:53 pm</span>
    <span class="charge">31%</span>
    <svg class="battery" width="52" height="20" viewBox="0 0 52 20">
      <rect x="1" y="1" width="46" height="18" rx="3" fill="none" stroke="#fff" stroke-width="1.5"/>
      <rect x="4" y="4" width="13" height="12" fill="#fff"/>
      <rect x="48" y="7" width="3" height="6" rx="1" fill="#fff"/>
    </svg>
  </div>

  <h1 class="greeting">Hello Mira !</h1>
  <h2 class="welcome">Welcome to QuizNest</h2>
  <p class="avatar-prompt">Please set your Avatar<br>so anyone can find you easily.&nbsp; :)</p>

  <div class="avatar" role="img" aria-label="Profile photo of the user"></div>

  <p class="pitch">QuizNest is Perfect app to improve<br>your knowledge Whether you are a<br>student or enthusiast</p>

  <div class="cta">Let’s Go</div>

  <div class="skip">Skip</div>
</main>
</body>
</html>
```